Kelbrook Aquatic Centre Open Day

FRONT PAGE

KELBROOK AQUATIC CENTRE OPEN DAY
31st May 2014
10am - 4pm
Free entry

Our Free Open Day is an event designed for the community to dive in and enjoy our great aquatic venue. There are plenty of activities for parents and kids to enjoy including the pool activities, free fitness classes and much more! Come join us on this great day to mark our 6 months of operation.

Sausage sizzle
pool activities
free group fitness classes
giveaways
door prizes

BACK PAGE
map of location
ph: 4731 5082
enquiries@kbaquatic-demo.com.au

want fitness and aquatic pics

plenty of colour - DL size
in your face kind of flyer

```html
<!DOCTYPE html>
<html lang="en">
<head>
<meta charset="utf-8">
<title>Kelbrook Aquatic Centre Open Day – DL Flyer</title>
<link href="https://fonts.googleapis.com/css2?family=Quicksand:wght@500;700&family=Tinos:ital,wght@0,700;1,400&display=swap" rel="stylesheet">
<style>
  :root {
    --teal: #3aa3bb;
    --teal-deep: #2a8aa3;
    --teal-light: #5bbfd3;
    --pool-blue: #4fa9c6;
    --white: #ffffff;
    --grey-band: #a3a5a8;
    --ink-dark: #1d4b5a;
    --stage: #e6e6e4;
    --map-base: #ecebe6;
  }
  * { box-sizing: border-box; margin: 0; padding: 0; }
  html, body { width: 1200px; height: 1200px; overflow: hidden; }
  body { background: var(--stage); position: relative; font-family: "Quicksand", sans-serif; }

  .flyer {
    position: absolute; top: 102px; width: 488px; height: 975px;
    overflow: hidden; background: var(--teal);
    box-shadow: 0 2px 8px rgba(0,0,0,.25);
  }
  .flyer--front { left: 92px; }
  .flyer--back { left: 605px; background: var(--white); }

  /* front */
  .front-waves { position: absolute; top: 0; left: 0; width: 488px; height: 360px; }
  .brand-name {
    position: absolute; top: 95px; left: 0; width: 100%;
    text-align: center; color: var(--teal); font-weight: 700;
    font-size: 40px; line-height: 1.1; text-transform: uppercase; letter-spacing: 1px;
  }
  .intro {
    position: absolute; top: 369px; left: 20px; width: 448px;
    text-align: center; color: var(--white); font-weight: 700;
    font-size: 15px; line-height: 24.2px; letter-spacing: .4px;
  }
  .venue-photo {
    position: absolute; top: 560px; left: 0; width: 488px; height: 290px;
    background: linear-gradient(180deg, var(--teal) 0%, #6fb4c8 30%, #4b9fbe 60%, #2f86ad 100%);
  }
  .activities {
    position: absolute; top: 563px; left: 0; width: 100%;
    list-style: none; text-align: center;
    font-family: "Tinos", serif; font-style: italic; color: var(--white);
    font-size: 23px; letter-spacing: 1px; text-transform: uppercase;
    text-shadow: 0 1px 3px rgba(0,40,60,.6);
  }
  .activities li { height: 43px; line-height: 30px; }
  .torn-edge { position: absolute; top: 808px; left: 0; width: 488px; height: 50px; }
  .event-band {
    position: absolute; top: 840px; left: 0; width: 100%; height: 135px;
    background: var(--grey-band); text-align: center; font-family: "Tinos", serif; font-weight: 700;
    color: var(--white); text-transform: uppercase;
  }
  .event-band .event-title { margin-top: 22px; font-size: 18px; letter-spacing: .6px; }
  .event-band .event-when { margin-top: 6px; font-size: 18px; letter-spacing: .6px; word-spacing: 4px; }
  .event-band .event-when span { margin-left: 18px; }
  .event-band .event-price { margin-top: 8px; font-size: 34px; color: var(--ink-dark); letter-spacing: 1px; }

  /* back */
  .back-header { position: absolute; top: 0; left: 0; width: 488px; height: 165px; }
  .phone {
    position: absolute; top: 30px; left: 0; width: 100%; text-align: center;
    color: var(--white); font-weight: 700; font-size: 23px; letter-spacing: 2px;
  }
  .photo { position: absolute; }
  .photo--class { top: 175px; left: 0; width: 234px; height: 234px; background: linear-gradient(160deg, #d9c9a6, #8fb8b4 60%, #6aa7ad); }
  .photo--underwater { top: 175px; left: 248px; width: 240px; height: 234px; background: linear-gradient(180deg, #5cb6d9, #2f86b8 60%, #3b93c0); }
  .photo--float { top: 422px; left: 0; width: 290px; height: 168px; background: linear-gradient(135deg, #3f8ca1, #2a6f86 55%, #4c97a8); }
  .photo--hall { top: 422px; left: 301px; width: 187px; height: 168px; background: linear-gradient(180deg, #e7ecef, #9cc7da 45%, #3d93c2); }
  .map {
    position: absolute; top: 603px; left: 0; width: 488px; height: 372px;
    background: linear-gradient(135deg, var(--map-base), #dcdcd6 50%, #f1f0e9);
  }
  .back-footer { position: absolute; top: 885px; left: 0; width: 488px; height: 90px; }
  .email {
    position: absolute; top: 945px; left: 32px; color: var(--white);
    font-weight: 700; font-size: 16px; letter-spacing: .5px;
  }
</style>
</head>
<body>

<section class="flyer flyer--front" aria-label="Flyer front">
  <svg class="front-waves" viewBox="0 0 488 360" aria-hidden="true">
    <path d="M0 0 H488 V200 C400 200 330 250 260 290 C200 320 130 300 90 250 L0 220 Z" fill="var(--white)"/>
    <path d="M90 245 C140 320 230 340 300 300 C360 265 420 215 488 205 V235 C420 240 370 290 300 330 C220 370 130 330 90 245 Z" fill="var(--teal-light)"/>
    <path d="M0 220 C40 230 70 240 90 248 C60 250 30 240 0 238 Z" fill="var(--teal-deep)" opacity=".6"/>
  </svg>
  <div class="brand-name">Kelbrook<br>Aquatic Centre</div>

  <p class="intro">Our Free Open Day is an event designed for the community to dive in and enjoy our great aquatic venue. There are plenty of activities for parents and kids to enjoy including the pool activities, free fitness classes and much more! Come join us on this great day to mark our 6 months of operation.</p>

  <div class="venue-photo" role="img" aria-label="Photo of the indoor lap pool hall with arched roof and lane ropes"></div>

  <ul class="activities">
    <li>Sausage Sizzle</li>
    <li>Pool Activities</li>
    <li>Free Group Fitness Classes</li>
    <li>Giveaways</li>
    <li>Door Prizes</li>
  </ul>

  <svg class="torn-edge" viewBox="0 0 488 50" preserveAspectRatio="none" aria-hidden="true">
    <path d="M0 20 L20 14 L40 22 L60 12 L85 20 L110 10 L130 24 L150 14 L175 22 L200 12 L225 25 L250 14 L275 20 L300 10 L325 24 L350 15 L375 22 L400 12 L425 20 L450 10 L470 22 L488 14 V50 H0 Z" fill="var(--white)"/>
    <path d="M0 30 L25 26 L50 34 L80 28 L110 34 L140 27 L170 35 L200 28 L230 34 L260 27 L290 35 L320 28 L350 34 L380 27 L410 35 L440 28 L470 33 L488 29 V50 H0 Z" fill="var(--grey-band)"/>
  </svg>

  <div class="event-band">
    <p class="event-title">Kelbrook Aquatic Centre Open Day</p>
    <p class="event-when">31st May 2014 <span>10am - 4pm</span></p>
    <p class="event-price">Free Entry</p>
  </div>
</section>

<section class="flyer flyer--back" aria-label="Flyer back">
  <svg class="back-header" viewBox="0 0 488 165" aria-hidden="true">
    <rect width="488" height="165" fill="var(--teal)"/>
    <path d="M0 115 C120 140 230 80 340 95 C410 105 450 110 488 100 V165 H0 Z" fill="var(--teal-deep)"/>
    <path d="M0 140 C130 160 250 120 360 130 C420 135 460 140 488 130 V165 H0 Z" fill="var(--white)"/>
  </svg>
  <p class="phone">PHONE : 4731 5082</p>

  <div class="photo photo--class" role="img" aria-label="Photo of an instructor leading an aqua fitness class from the pool deck"></div>
  <div class="photo photo--underwater" role="img" aria-label="Underwater photo of swimmers doing aqua aerobics"></div>
  <div class="photo photo--float" role="img" aria-label="Photo of a swimmer floating with foam dumbbells"></div>
  <div class="photo photo--hall" role="img" aria-label="Photo of the lap pool hall with arched roof"></div>

  <div class="map" role="img" aria-label="Street map showing the location of the aquatic centre"></div>

  <svg class="back-footer" viewBox="0 0 488 90" aria-hidden="true">
    <path d="M0 25 C100 5 200 10 300 25 C380 38 440 30 488 20 V90 H0 Z" fill="var(--teal-deep)"/>
    <path d="M0 35 C110 15 210 22 310 38 C390 50 440 42 488 32 V90 H0 Z" fill="var(--teal)"/>
  </svg>
  <p class="email">enquiries@kbaquatic-demo.com.au</p>
</section>

</body>
</html>
```